Forking Well Buisiness card

needing a Business card for our company - Forking Well.
Forking well is co owned by Jess and Owen Marchetti (Husband and Wife)
Services Forking Well provides include:
Dietetic/nutrition Consultations, weight loss coaching programs, personal and group training, post injury rehab, health and nutrition presentations and Health Retreats.
Jess:
Accredited Practicing Dietitian & Personal trainer
Owen:
Personal trainer, rehab trainer & Strength and conditioning coach
At this stage the business cards will be made just for Jess.
She has a training studio in Armadale and Dietetics private practice in Richmond.
Mobile services are also available (i.e. meet at house or local cafe)

We need the card to look smart, modern and combine both nutrition and training.
We already have a logo which I will attach.
I was initial thinking i black background but am open to suggestions.

Target Market(s)

Health concious, People with money,

Industry/Entity Type

Nutrition

Contact Information for Business Card

Forking Well
Jess Marchetti
M: 0417390265
E: forkingwell@mailnest.com
W: www.forkingwell.com.au
Address:
Dietetics: Level 1, 583 Bellow Street
Richmond VIC 3121
Training: Private Studio, behind 2087 Tamsin St
ARMADALE, VIC, 3143

Requirements
Must have
• Must have logo (see attached) please not the one we use is the top left (blue and green)
please note attachment is top left (green and blue)

needs to be clear to read - the font needs to be clear and sharp and the background cannot be too busy.eg funny patterns.
Could I please see a card with a line for 'appointment time/date:' possibly on the back. Would like to see what this looks like.
Jess Marchetti's Profile (side of card) must include "Accredited Practicing Dietitian" and "Personal Trainer."
I like when the services forking well provide are in dot form.
Nice to have
• would like the card to be 2 sides
first side:
Forking well logo - Large
services forking well provides: Dietetic/nutrition Consultations, weight loss coaching programs, personal and group training, post injury rehab, health and nutrition presentations and Health Retreats.
web address
second side:
smaller logo
Details for Jess:
Accredited Practicing Dietitian
Personal Trainer
Contact Details:
M: 0417390265
E: forkingwell@mailnest.com
Address:
Richmond VIC 3121
ARMADALE, VIC, 3143
Should not have
• Dietetic + nutrition consultations
Should say dietetic/nutrition consultations (first letter of words in capitals please)
Please write phone number as 0417 390 265
Not: 04 17 390265
- note numbers as 4, 3, 3.

```html
<!DOCTYPE html>
<html lang="en">
<head>
<meta charset="utf-8">
<title>Forking Well Business Card</title>
<link href="https://fonts.googleapis.com/css2?family=Open+Sans:ital,wght@0,400;0,600;0,700;1,400&display=swap" rel="stylesheet">
<style>
  :root{
    --bg:#e9e6e1;
    --card:#0d0d0e;
    --card-edge:#1c1c1f;
    --green:#8cc63f;
    --blue:#1f5fbf;
    --blue-dark:#174a96;
    --text:#f2f2f2;
    --muted:#b9b9b9;
    --ghost:#3a3a3d;
  }
  *{box-sizing:border-box;margin:0;padding:0}
  html,body{width:1200px;height:1024px;overflow:hidden}
  body{background:var(--bg);font-family:"Open Sans",Arial,sans-serif;color:var(--text)}
  .card{position:absolute;left:220px;width:760px;height:460px;background:var(--card);
        border-radius:4px;overflow:hidden;box-shadow:0 10px 30px rgba(0,0,0,.25)}
  .card--contact{top:36px}
  .card--services{top:528px}
  .card svg.wave{position:absolute;inset:0;width:100%;height:100%}
  .brand{position:absolute;display:flex;align-items:center;gap:14px}
  .brand__dot{width:22px;height:22px;border-radius:50%;background:var(--green)}
  .brand__name{font-weight:600;color:var(--blue);line-height:1}
  .tagline{position:absolute;font-style:italic;color:var(--muted);font-size:15px}
  /* contact side */
  .card--contact .brand{left:56px;top:58px}
  .card--contact .brand__name{font-size:50px}
  .card--contact .tagline{left:92px;top:122px}
  .divider{position:absolute;left:372px;top:112px;width:2px;height:52px;background:var(--green);transform:rotate(35deg)}
  .profile{position:absolute;left:56px;top:282px;font-size:16px;line-height:1.45}
  .profile__name{color:var(--green);font-weight:700;font-size:24px;line-height:1.2}
  .profile__role{color:var(--blue)}
  .profile__studio{color:var(--text)}
  .profile__studio .label{color:var(--green)}
  .contact{position:absolute;left:440px;top:40px;font-size:15px;line-height:1.6}
  .contact .label{color:var(--green)}
  .web{position:absolute;color:var(--text);font-size:17px;font-weight:600}
  .card--contact .web{right:60px;bottom:40px}
  /* services side */
  .card--services .brand{left:70px;top:44px}
  .card--services .brand__name{font-size:54px;color:var(--text)}
  .card--services .brand__dot{width:26px;height:26px}
  .card--services .tagline{left:150px;top:112px}
  .services{position:absolute;left:70px;top:150px;font-size:15px;line-height:1.55}
  .services__title{color:var(--green);font-weight:700;font-style:italic;margin-bottom:4px}
  .services ul{list-style:none}
  .services li::before{content:"•";color:var(--green);margin-right:9px}
  .card--services .web{left:56px;bottom:34px}
  .emblem{position:absolute;right:-30px;bottom:-50px;width:380px;height:250px;border-radius:50%;
          background:radial-gradient(ellipse at center,#2a2a2d 0%,#161618 70%,transparent 72%)}
</style>
</head>
<body>

<section class="card card--contact">
  <svg class="wave" viewBox="0 0 760 460" preserveAspectRatio="none" aria-hidden="true">
    <path d="M760 150 C600 190 480 300 360 460 L760 460 Z" fill="var(--green)"/>
    <path d="M760 172 C610 210 500 310 392 460 L760 460 Z" fill="var(--card)"/>
    <path d="M760 186 C620 224 520 320 418 460 L760 460 Z" fill="var(--blue)"/>
  </svg>
  <div class="brand"><span class="brand__dot"></span><span class="brand__name">Forking Well</span></div>
  <p class="tagline">"It's what you put in!"</p>
  <span class="divider"></span>
  <div class="profile">
    <p class="profile__name">Jess Marchetti</p>
    <p class="profile__role">Accredited Practicing Dietitian<br>&amp; Personal Trainer</p>
    <p class="profile__studio"><span class="label">Training :</span> Private Studio,<br>behind 2087 Tamsin St Armadale, VIC, 3143</p>
  </div>
  <div class="contact">
    <p><span class="label">M:</span> 0417 390 265</p>
    <p><span class="label">E:</span> forkingwell@mailnest.com</p>
    <p><span class="label">Add:</span> Dietetics: Level 1,</p>
    <p>583 Bellow Street Richmond VIC 3121</p>
  </div>
  <p class="web">www.forkingwell.com.au</p>
</section>

<section class="card card--services">
  <svg class="wave" viewBox="0 0 760 460" preserveAspectRatio="none" aria-hidden="true">
    <path d="M0 300 C140 330 250 380 340 460 L0 460 Z" fill="var(--green)"/>
    <path d="M0 318 C130 346 236 392 318 460 L0 460 Z" fill="var(--card)"/>
    <path d="M0 330 C124 356 226 400 300 460 L0 460 Z" fill="var(--blue)"/>
  </svg>
  <div class="emblem" role="img" aria-label="Large faint brand emblem of a running figure"></div>
  <div class="brand"><span class="brand__dot"></span><span class="brand__name">Forking Well</span></div>
  <p class="tagline">"It's what you put in!"</p>
  <div class="services">
    <p class="services__title">Services Forking Well provides include:</p>
    <ul>
      <li>Dietetic/Nutrition Consultations,</li>
      <li>Weight Loss Coaching Programs,</li>
      <li>Personal and Group Training,</li>
      <li>Post Injury Rehab,</li>
      <li>Health and Nutrition Presentations</li>
      <li>Health Retreats</li>
    </ul>
  </div>
  <p class="web">www.forkingwell.com.au</p>
</section>

</body>
</html>
```